Employee Portal UI Design - Modern and Clean

We are an agency tasked with developing a team portal for a company that has many employees. As we embark on this project, we seek a great UI design to accompany the requirements our client has for this project. We already have several screens mocked up that can be used as reference for the overall idea. Currently, we are only looking for the main dashboard's home page, user registration screen, and account settings page to be designed. The main brand colors are red but other accents can be used as well. The client's vision is for modern & minimalist to be at the center. We have a specific font to be used, but if you don't have access to it, you can just use a similar font.Main color: #DD0031The sub menus (do not need to be designed) would be:>Performance Reviews>Posts>Team directory>Calendar>Tasks>Documents>LinksWe would prefer the design be made in Adobe XD.

Industry/Entity Type

Fast Food Restaurant

Number of Pages Required

1 page

Font styles to use
Sans Serif

Colors
ec1f27

Requirements
Must have
• Color: #DD0031 (highlights)

```html
<!DOCTYPE html>
<html lang="en">
<head>
<meta charset="utf-8">
<title>Employee Portal UI</title>
<link href="https://fonts.googleapis.com/css2?family=Roboto:wght@400;500;700&display=swap" rel="stylesheet">
<style>
:root{
  --red:#e41e2b;
  --red-soft:#fdeaea;
  --ink:#1c1c1c;
  --text:#3a3a3a;
  --muted:#9a9a9a;
  --faint:#c4c4c4;
  --line:#ececec;
  --panel:#f8f8f8;
  --purple:#6b5ca5;
  --orange:#f2a93b;
  --photo-a:#5f6a74;
  --photo-b:#a9a39a;
}
*{box-sizing:border-box;margin:0;padding:0}
html,body{width:1200px;height:1200px;overflow:hidden;background:#fff;font-family:'Roboto',sans-serif;color:var(--text)}
.stage{position:relative;width:1500px;height:1500px;transform:scale(.8);transform-origin:0 0;background:linear-gradient(90deg,#f5f5f5 0 390px,#fff 390px)}
.screen{position:absolute;width:920px;height:575px;background:#fff;border-radius:50px;overflow:hidden;box-shadow:0 14px 40px rgba(0,0,0,.09)}
.abs{position:absolute}
.screen--signup{left:290px;top:825px;z-index:1}
.screen--settings{left:480px;top:462px;z-index:2}
.screen--dashboard{left:100px;top:100px;z-index:3}

.sidebar{position:absolute;left:0;top:0;width:100px;height:100%;border-right:1px solid var(--line);background:#fff}
.burger{position:absolute;left:37px;top:23px;width:19px}
.burger i{display:block;height:1.5px;background:var(--text);margin-bottom:6px}
.burger i:nth-child(2){width:12px}
.nav{position:absolute;left:0;top:94px;width:100px;list-style:none}
.nav li{height:34.5px;display:flex;align-items:center;font-size:8.5px;color:#555;padding-left:13px;gap:10px;line-height:1.1}
.nav li svg{width:17px;height:17px;flex:none;fill:none;stroke:#888;stroke-width:1.1}
.nav li.is-active{height:22px;margin:6px 0 6.5px;background:var(--red-soft);color:var(--red);font-weight:500;border-right:2px solid var(--red)}
.nav li.is-active svg{stroke:var(--red)}

.topbar{position:absolute;left:552px;top:0;width:368px;height:58px;border-bottom:1px solid var(--line);display:flex}
.topbar .cell{height:100%;display:flex;align-items:center;justify-content:center;border-left:1px solid var(--line)}
.topbar .dots{width:63px}
.topbar .dots i{width:4px;height:4px;border-radius:50%;background:#555;margin:0 1.5px}
.topbar .bell{width:65px}
.topbar .user{flex:1;justify-content:flex-start;padding-left:44px;gap:14px;font-size:12px;color:var(--ink)}
.avatar{border-radius:50%;background:linear-gradient(135deg,var(--photo-b),var(--photo-a))}
.topbar .avatar{width:28px;height:28px}
.chev{margin-left:auto;margin-right:40px}

/* dashboard */
.logo{left:278px;top:17px;width:98px;height:24px;border-radius:12px;background:var(--red-soft);color:var(--red);font-size:11px;display:flex;align-items:center;justify-content:center;letter-spacing:.3px}
.main-head{left:100px;top:57px;width:452px;border-top:1px solid var(--line)}
.search{left:100px;top:58px;width:452px;height:36px;border-bottom:1px solid var(--line);display:flex;align-items:center;padding-left:42px;gap:14px;font-size:8px;color:var(--faint)}
.section-title{left:143px;top:109px;font-size:15px;font-weight:700;color:var(--ink)}
.activity{position:absolute;left:143px;width:358px;height:108px;border:1px solid var(--line);border-radius:4px;padding:10px 13px;background:#fff}
.activity .meta{display:flex;align-items:center;font-size:8px;color:var(--muted);gap:8px}
.activity .meta .avatar{width:17px;height:17px}
.activity .meta time{margin-left:auto}
.activity .meta time b{font-weight:400;color:#555}
.activity h3{font-size:12.5px;color:var(--red);font-weight:500;margin-top:10px}
.activity .sub{font-size:10px;color:var(--ink);margin-top:5px}
.activity .body{font-size:8px;color:var(--faint);line-height:1.25;margin-top:8px}
.fab{left:482px;top:514px;width:40px;height:40px;border-radius:50%;background:var(--red);box-shadow:0 6px 14px rgba(228,30,43,.35);display:flex;align-items:center;justify-content:center}
.right-panel{left:552px;top:0;width:368px;height:575px;border-left:1px solid var(--line)}
.cal-head{left:576px;top:70px;width:322px;display:flex;justify-content:space-between;align-items:center;font-size:12px;color:var(--red);padding:0 16px}
.cal{left:576px;top:100px;width:322px;display:grid;grid-template-columns:repeat(7,46px);text-align:center;font-size:9.5px;color:var(--ink)}
.cal .wd{font-size:8.5px;color:var(--faint);height:32px;line-height:18px}
.cal .d{height:31px;position:relative;line-height:18px}
.cal .d.out{color:var(--faint)}
.cal .d.today span{display:inline-block;width:18px;height:18px;border-radius:50%;background:var(--red);color:#fff}
.cal .mk{position:absolute;left:0;right:0;top:16px;display:flex;justify-content:center;gap:2px}
.cal .mk i{width:4px;height:4px;border-radius:50%}
.mk .e{background:var(--purple)}
.mk .t{border:1px solid var(--orange)}
.legend{top:292px;font-size:8px;color:#666;display:flex;align-items:center;gap:10px}
.legend i{width:4px;height:4px;border-radius:50%}
.agenda-line{left:552px;width:368px;border-top:1px solid var(--line)}
.col{position:absolute;top:324px;width:184px;height:251px}
.col h4{position:absolute;left:53px;top:14px;font-size:11px;font-weight:700;color:var(--ink);letter-spacing:.2px}
.col .day{position:absolute;left:53px;font-size:11px}
.col .day small{font-size:8px}
.col .item{position:absolute;left:53px;font-size:8px;font-weight:500;color:var(--ink)}
.col .item span{display:block;font-weight:400;color:var(--faint);margin-top:6px}
.col .item:before{content:"";position:absolute;left:-13px;top:10px;width:4px;height:4px;border-radius:50%}
.col--events .day{color:var(--purple)}
.col--events .item:before{background:var(--purple)}
.col--tasks .day{color:var(--orange)}
.col--tasks .item:before{border:1px solid var(--orange)}
.more{position:absolute;left:53px;top:314px;font-size:8px;display:flex;align-items:center;gap:8px}

/* forms */
.canvas-bg{left:100px;top:58px;width:820px;height:517px;background:var(--panel)}
.card{left:118px;top:71px;width:802px;height:504px;background:#fff}
.field{position:absolute;width:184px;height:37px;border:1px solid var(--line);border-radius:3px;background:#fffdfd;padding:5px 12px;font-size:10.5px;color:var(--ink)}
.field label{display:block;font-size:7.5px;color:var(--faint);margin-bottom:3px}
.field--plain{display:flex;align-items:center;font-weight:500}
.field--plain em{font-style:normal;color:var(--red);margin-left:3px}
.rule{width:460px;border-top:1px solid var(--line)}
.form-title{font-size:11.5px;font-weight:500;color:var(--ink)}
.btn{position:absolute;width:91px;height:30px;border-radius:4px;background:var(--red);color:#fff;font-size:12px;font-weight:700;display:flex;align-items:center;justify-content:center;box-shadow:0 6px 12px rgba(228,30,43,.25)}
.photo{width:84px;height:84px;border-radius:50%}
.edit{width:22px;height:22px;border-radius:50%;background:#333;border:2px solid #fff;display:flex;align-items:center;justify-content:center}
.tabs{top:142px;font-size:8px;color:#555;font-weight:500}
</style>
</head>
<body>
<div class="stage">

  <!-- Sign up screen -->
  <section class="screen screen--signup">
    <aside class="sidebar">
      <div class="burger"><i></i><i></i><i></i></div>
      <ul class="nav">
        <li class="is-active"><svg viewBox="0 0 18 18"><path d="M2 9l7-6 7 6M4 7.5V15h10V7.5"/></svg>Home</li>
        <li><svg viewBox="0 0 18 18"><path d="M9 2l2.1 4.5 4.9.6-3.6 3.3 1 4.8L9 12.8 4.6 15.2l1-4.8L2 7.1l4.9-.6z"/></svg>Reviews</li>
        <li><svg viewBox="0 0 18 18"><path d="M3 15l1-4 8-8 3 3-8 8zM2 16h14"/></svg>Posts</li>
        <li><svg viewBox="0 0 18 18"><circle cx="9" cy="4" r="2"/><circle cx="4" cy="12" r="2"/><circle cx="14" cy="12" r="2"/><path d="M9 6v3M5 10l3-1M13 10l-3-1"/></svg>Team<br>Directory</li>
        <li><svg viewBox="0 0 18 18"><rect x="2" y="3" width="14" height="13"/><path d="M2 7h14M5 1v4M13 1v4"/></svg>Calendar</li>
        <li><svg viewBox="0 0 18 18"><path d="M2 15V5h5l2 2h7v8zM5 5V3h8v4"/></svg>Tasks</li>
        <li><svg viewBox="0 0 18 18"><path d="M4 2h7l3 3v11H4zM6 8h6M6 11h6M6 14h4"/></svg>Documents</li>
        <li><svg viewBox="0 0 18 18"><path d="M7 11l4-4M6 9l-2 2a2.5 2.5 0 003.5 3.5l2-2M12 9l2-2A2.5 2.5 0 0010.5 3.5l-2 2"/></svg>Links</li>
      </ul>
    </aside>
    <div class="abs" style="left:100px;top:57px;width:820px;border-top:1px solid var(--line)"></div>
    <div class="abs canvas-bg"></div>
    <div class="abs" style="left:118px;top:70px;width:802px;height:505px;background:#fff"></div>
    <div class="abs form-title" style="left:185px;top:97px;font-size:14px;font-weight:700">Profile</div>
    <div class="abs form-title" style="left:186px;top:195px">Profile</div>
    <div class="abs photo" style="left:185px;top:229px;background:#f3f3f3;border:1px solid var(--line)">
      <svg viewBox="0 0 84 84" width="84" height="84"><circle cx="42" cy="32" r="15" fill="#d8d8d8"/><path d="M19 84V62c0-6 5-10 11-10h24c6 0 11 4 11 10v22z" fill="#d8d8d8"/></svg>
    </div>
    <div class="abs edit" style="left:248px;top:224px"><svg width="10" height="10" viewBox="0 0 10 10"><path d="M1 9l1-3 5-5 2 2-5 5z" fill="none" stroke="#fff" stroke-width="1"/></svg></div>
    <div class="field field--plain" style="left:369px;top:224px">Name<em>*</em></div>
    <div class="field field--plain" style="left:645px;top:224px">Last Name<em>*</em></div>
    <div class="field field--plain" style="left:369px;top:282px">Email Address<em>*</em></div>
    <div class="field field--plain" style="left:645px;top:282px">Phone Number<em>*</em></div>
    <div class="field field--plain" style="left:369px;top:339px">City</div>
    <div class="field field--plain" style="left:645px;top:339px">State</div>
    <div class="abs rule" style="left:369px;top:399px"></div>
    <div class="abs form-title" style="left:369px;top:417px">Password</div>
    <div class="field field--plain" style="left:369px;top:446px">Password<em>*</em></div>
    <div class="field field--plain" style="left:645px;top:446px">Repeat Password<em>*</em></div>
    <div class="abs" style="left:369px;top:517px;font-size:8px;color:var(--red)">* required fields</div>
    <div class="btn" style="left:737px;top:507px">Sign Up</div>
  </section>

  <!-- Account settings screen -->
  <section class="screen screen--settings">
    <aside class="sidebar">
      <ul class="nav">
        <li class="is-active"><svg viewBox="0 0 18 18"><path d="M2 9l7-6 7 6M4 7.5V15h10V7.5"/></svg>Home</li>
        <li><svg viewBox="0 0 18 18"><path d="M9 2l2.1 4.5 4.9.6-3.6 3.3 1 4.8L9 12.8 4.6 15.2l1-4.8L2 7.1l4.9-.6z"/></svg>Reviews</li>
        <li><svg viewBox="0 0 18 18"><path d="M3 15l1-4 8-8 3 3-8 8zM2 16h14"/></svg>Posts</li>
        <li><svg viewBox="0 0 18 18"><circle cx="9" cy="4" r="2"/><circle cx="4" cy="12" r="2"/><circle cx="14" cy="12" r="2"/><path d="M9 6v3M5 10l3-1M13 10l-3-1"/></svg>Team<br>Directory</li>
        <li><svg viewBox="0 0 18 18"><rect x="2" y="3" width="14" height="13"/><path d="M2 7h14M5 1v4M13 1v4"/></svg>Calendar</li>
        <li><svg viewBox="0 0 18 18"><path d="M2 15V5h5l2 2h7v8zM5 5V3h8v4"/></svg>Tasks</li>
        <li><svg viewBox="0 0 18 18"><path d="M4 2h7l3 3v11H4zM6 8h6M6 11h6M6 14h4"/></svg>Documents</li>
        <li><svg viewBox="0 0 18 18"><path d="M7 11l4-4M6 9l-2 2a2.5 2.5 0 003.5 3.5l2-2M12 9l2-2A2.5 2.5 0 0010.5 3.5l-2 2"/></svg>Links</li>
      </ul>
    </aside>
    <div class="abs canvas-bg"></div>
    <div class="abs card"></div>
    <div class="topbar">
      <div class="cell dots"><i></i><i></i><i></i></div>
      <div class="cell bell"><svg width="20" height="22" viewBox="0 0 20 22" fill="none" stroke="#555" stroke-width="1.2"><path d="M4 16V9a6 6 0 0112 0v7l2 2H2zM8 20h4"/></svg></div>
      <div class="cell user"><div class="avatar" role="img" aria-label="Profile photo of Alex Marlow"></div>Alex Marlow<svg class="chev" width="12" height="8" viewBox="0 0 12 8"><path d="M1 1l5 5 5-5" fill="none" stroke="#e41e2b" stroke-width="2"/></svg></div>
    </div>
    <div class="abs tabs" style="left:585px">Custom Links</div>
    <div class="abs tabs" style="left:689px">Plan &amp; Billing</div>
    <div class="abs rule" style="left:368px;top:167px"></div>
    <div class="abs photo avatar" style="left:185px;top:229px" role="img" aria-label="Profile photo of Alex Marlow"></div>
    <div class="abs edit" style="left:247px;top:225px"><svg width="10" height="10" viewBox="0 0 10 10"><path d="M1 9l1-3 5-5 2 2-5 5z" fill="none" stroke="#fff" stroke-width="1"/></svg></div>
    <div class="field" style="left:368px;top:225px"><label>Name:</label>Alex</div>
    <div class="field" style="left:645px;top:225px"><label>Last Name:</label>Marlow</div>
    <div class="field" style="left:368px;top:282px"><label>Email:</label>alex.marlow@mailbox.test</div>
    <div class="field" style="left:645px;top:282px"><label>Phone Number:</label>(+38) 555 010 203</div>
    <div class="field" style="left:368px;top:340px"><label>City:</label>Brookvale</div>
    <div class="field" style="left:645px;top:340px"><label>State:</label>Westmark</div>
    <div class="abs rule" style="left:368px;top:399px"></div>
    <div class="abs form-title" style="left:368px;top:417px">Change Password</div>
    <div class="field" style="left:368px;top:446px"><label>Current Password</label>*********</div>
    <div class="field" style="left:645px;top:446px"><label>New Password</label>**********</div>
    <div class="btn" style="left:737px;top:508px">Save</div>
  </section>

  <!-- Dashboard home screen -->
  <section class="screen screen--dashboard">
    <aside class="sidebar">
      <div class="burger"><i></i><i></i><i></i></div>
      <ul class="nav">
        <li class="is-active"><svg viewBox="0 0 18 18"><path d="M2 9l7-6 7 6M4 7.5V15h10V7.5"/></svg>Home</li>
        <li><svg viewBox="0 0 18 18"><path d="M9 2l2.1 4.5 4.9.6-3.6 3.3 1 4.8L9 12.8 4.6 15.2l1-4.8L2 7.1l4.9-.6z"/></svg>Reviews</li>
        <li><svg viewBox="0 0 18 18"><path d="M3 15l1-4 8-8 3 3-8 8zM2 16h14"/></svg>Posts</li>
        <li><svg viewBox="0 0 18 18"><circle cx="9" cy="4" r="2"/><circle cx="4" cy="12" r="2"/><circle cx="14" cy="12" r="2"/><path d="M9 6v3M5 10l3-1M13 10l-3-1"/></svg>Team<br>Directory</li>
        <li><svg viewBox="0 0 18 18"><rect x="2" y="3" width="14" height="13"/><path d="M2 7h14M5 1v4M13 1v4"/></svg>Calendar</li>
        <li><svg viewBox="0 0 18 18"><path d="M2 15V5h5l2 2h7v8zM5 5V3h8v4"/></svg>Tasks</li>
        <li><svg viewBox="0 0 18 18"><path d="M4 2h7l3 3v11H4zM6 8h6M6 11h6M6 14h4"/></svg>Documents</li>
        <li><svg viewBox="0 0 18 18"><path d="M7 11l4-4M6 9l-2 2a2.5 2.5 0 003.5 3.5l2-2M12 9l2-2A2.5 2.5 0 0010.5 3.5l-2 2"/></svg>Links</li>
      </ul>
    </aside>

    <div class="abs logo">LOGO</div>
    <div class="abs main-head"></div>
    <div class="abs search"><svg width="14" height="14" viewBox="0 0 14 14" fill="none" stroke="#ccc" stroke-width="1.2"><circle cx="6" cy="6" r="4.5"/><path d="M9.5 9.5L13 13"/></svg>Search...</div>
    <h2 class="abs section-title">Recent Activities</h2>

    <article class="activity" style="top:149px">
      <div class="meta"><span class="avatar" role="img" aria-label="Profile photo"></span>Alex Marlow<time>Friday 01.03, <b>11:00 AM</b></time></div>
      <h3>New Performance Review</h3>
      <p class="sub">Performance Review for Alex Marlow</p>
      <p class="body">Lorem ipsum dolor sit amet, consectetur adipiscing elit, sed do eiusmod tempor incididunt ut labore et dolore magna aliqua. Ut enim ad minim veniam, quis nostrud</p>
    </article>
    <article class="activity" style="top:276px">
      <div class="meta"><span class="avatar" role="img" aria-label="Profile photo"></span>Alex Marlow<time>Friday 01.03, <b>11:00 AM</b></time></div>
      <h3>New Performance Review</h3>
      <p class="sub">Performance Review for Alex Marlow</p>
      <p class="body">Lorem ipsum dolor sit amet, consectetur adipiscing elit, sed do eiusmod tempor incididunt ut labore et dolore magna aliqua. Ut enim ad minim veniam, quis nostrud</p>
    </article>
    <article class="activity" style="top:403px">
      <div class="meta"><span class="avatar" role="img" aria-label="Profile photo"></span>Alex Marlow<time>Friday 01.03, <b>11:00 AM</b></time></div>
      <h3>New Performance Review</h3>
      <p class="sub">Performance Review for Alex Marlow</p>
      <p class="body">Lorem ipsum dolor sit amet, consectetur adipiscing elit, sed do eiusmod tempor incididunt ut labore et dolore magna aliqua. Ut enim ad minim veniam, quis nostrud</p>
    </article>
    <div class="abs fab"><svg width="16" height="16" viewBox="0 0 16 16"><path d="M8 1v14M1 8h14" stroke="#fff" stroke-width="2.4"/></svg></div>

    <div class="abs right-panel"></div>
    <div class="topbar">
      <div class="cell dots"><i></i><i></i><i></i></div>
      <div class="cell bell"><svg width="20" height="22" viewBox="0 0 20 22" fill="none" stroke="#555" stroke-width="1.2"><path d="M4 16V9a6 6 0 0112 0v7l2 2H2zM8 20h4"/></svg></div>
      <div class="cell user"><div class="avatar" role="img" aria-label="Profile photo of Alex Marlow"></div>Alex Marlow<svg class="chev" width="12" height="8" viewBox="0 0 12 8"><path d="M1 1l5 5 5-5" fill="none" stroke="#e41e2b" stroke-width="2"/></svg></div>
    </div>

    <div class="abs cal-head"><span>&lt;</span>March 2019<span>&gt;</span></div>
    <div class="abs cal">
      <div class="wd">M</div><div class="wd">T</div><div class="wd">W</div><div class="wd">T</div><div class="wd">F</div><div class="wd">S</div><div class="wd">S</div>
      <div class="d out">25</div><div class="d out">26</div><div class="d out">27</div><div class="d out">28</div><div class="d">1</div><div class="d">2</div><div class="d today"><span>3</span></div>
      <div class="d">4<div class="mk"><i class="e"></i><i class="t"></i></div></div>
      <div class="d">5<div class="mk"><i class="e"></i><i class="t"></i></div></div>
      <div class="d">6<div class="mk"><i class="t"></i></div></div>
      <div class="d">7<div class="mk"><i class="e"></i></div></div>
      <div class="d">8</div>
      <div class="d">9<div class="mk"><i class="t"></i></div></div>
      <div class="d">10<div class="mk"><i class="e"></i></div></div>
      <div class="d">11</div>
      <div class="d">12<div class="mk"><i class="e"></i><i class="t"></i></div></div>
      <div class="d">13</div><div class="d">14</div>
      <div class="d">15<div class="mk"><i class="e"></i></div></div>
      <div class="d">16</div><div class="d">17</div>
      <div class="d">18</div><div class="d">19</div>
      <div class="d">20<div class="mk"><i class="e"></i><i class="t"></i></div></div>
      <div class="d">21</div><div class="d">22</div><div class="d">23</div><div class="d">24</div>
      <div class="d">25</div><div class="d">26</div><div class="d">27</div><div class="d">28</div><div class="d">29</div><div class="d">30</div><div class="d">31</div>
    </div>
    <div class="abs legend" style="left:617px"><i style="background:var(--purple)"></i>Events</div>
    <div class="abs legend" style="left:795px"><i style="border:1px solid var(--orange)"></i>Tasks</div>

    <div class="abs agenda-line" style="top:324px"></div>
    <div class="abs agenda-line" style="top:381px"></div>
    <div class="abs agenda-line" style="top:489px"></div>
    <div class="abs" style="left:736px;top:324px;height:251px;border-left:1px solid var(--line)"></div>

    <div class="col col--events" style="left:552px">
      <h4>EVENTS</h4>
      <div class="day" style="top:39px">Tomorrow, <small>04.03</small></div>
      <div class="item" style="top:65px">Daily Safe Checklist<span>8:45 AM - 9:00 AM</span></div>
      <div class="item" style="top:102px">Director Meeting<span>10:00 AM - 11:00 AM</span></div>
      <div class="day" style="top:143px">Tuesday, <small>05.03</small></div>
      <div class="item" style="top:169px">Daddy Daughter Night<span>8:45 AM - 9:00 AM</span></div>
      <div class="more" style="top:214px;color:var(--purple)">See more<svg width="18" height="8" viewBox="0 0 18 8"><path d="M0 4h16M13 1l3 3-3 3" fill="none" stroke="currentColor"/></svg></div>
    </div>
    <div class="col col--tasks" style="left:736px;width:184px">
      <h4 style="left:29px">TASKS</h4>
      <div class="day" style="top:39px;left:29px">Tomorrow, <small>04.03</small></div>
      <div class="item" style="top:65px;left:29px">Daily Stand-Up<span>8:45 AM - 9:30 AM</span></div>
      <div class="item" style="top:102px;left:29px">Daily eRQA<span>10:00 AM - 11:00 AM</span></div>
      <div class="day" style="top:145px;left:29px">Tuesday, <small>05.03</small></div>
      <div class="item" style="top:171px;left:29px">Daily Safe Checklist<span>8:45 AM - 9:30 AM</span></div>
      <div class="more" style="top:214px;left:29px;color:var(--orange)">See more<svg width="18" height="8" viewBox="0 0 18 8"><path d="M0 4h16M13 1l3 3-3 3" fill="none" stroke="currentColor"/></svg></div>
    </div>
  </section>

</div>
</body>
</html>
```